University Student Business Card

Looking for a professional university student business card. Student is studying business with a focus on marketing. Some combination using a monogram and/or full name on the front with full name, university details and contact information on the back. Card should be modern design for a young professional. Prefer use of royal blue, black and white but am open to other uses of colour palette if it reinforces young/trendy style. Initials for a monogram are: KM. Full details will be provided in private consultation with designer(s).

Target Market(s)

Professional business people, marketers, advertisers, consultants

Industry/Entity Type

Business, marketing

Contact Information for Business Card

Monogram or personal logo, full name, university name, program of study, phone number, email address, linkedin address

Font styles to use
Other font styles liked:
• Open to suggestion to fulfill above requirements

Colors
0054AA
0677BA
7BADD7
CADEEF
E8F1F8

Requirements
Must have
• Monogram using letters K and M, and incorporate the business card details listed in the brief (specific details including personal contact info will be shared with successful designer to ensure privacy)
Nice to have
• Personal brand using monogram or personal logo (not a business logo)

```html
<!DOCTYPE html>
<html lang="en">
<head>
<meta charset="utf-8">
<title>KM Student Business Card</title>
<link href="https://fonts.googleapis.com/css2?family=Lato:wght@400;700&family=Arimo:wght@400&display=swap" rel="stylesheet">
<style>
  :root {
    --backdrop: #1e1e1e;
    --card: #0b0b0b;
    --royal-blue: #0054aa;
    --white: #f2f2f2;
    --grey: #bdbdbd;
    --rule: #555555;
  }
  * { box-sizing: border-box; margin: 0; padding: 0; }
  html, body { width: 1200px; height: 900px; overflow: hidden; }
  body {
    background: var(--backdrop);
    display: flex;
    align-items: center;
    justify-content: center;
    gap: 60px;
    font-family: "Arimo", Arial, sans-serif;
  }
  .card {
    width: 525px;
    height: 300px;
    background: var(--card);
    box-shadow: 0 10px 30px rgba(0,0,0,.6);
    display: flex;
    flex-direction: column;
    align-items: center;
    justify-content: center;
    text-align: center;
    color: var(--white);
  }
  .university-name {
    font-family: "Lato", Arial, sans-serif;
    font-weight: 700;
    font-size: 27px;
    letter-spacing: .5px;
    color: var(--royal-blue);
    line-height: 1;
  }
  .address {
    margin-top: 8px;
    font-size: 14.5px;
    line-height: 1.25;
    color: var(--grey);
    letter-spacing: .3px;
  }
  .divider {
    width: 95px;
    height: 1px;
    background: var(--rule);
    margin: 12px 0;
  }
  .contact {
    font-size: 16px;
    line-height: 1.3;
    letter-spacing: .4px;
    color: var(--white);
  }
  .contact .accent { color: var(--royal-blue); }

  .monogram {
    font-family: "Lato", Arial, sans-serif;
    font-weight: 700;
    font-size: 92px;
    line-height: 1;
    letter-spacing: 2px;
    color: var(--royal-blue);
    margin-bottom: 14px;
  }
  .person-name {
    font-family: "Lato", Arial, sans-serif;
    font-weight: 700;
    font-size: 20px;
    letter-spacing: .5px;
    color: var(--royal-blue);
    line-height: 1;
  }
  .program {
    margin-top: 4px;
    font-size: 13.5px;
    color: var(--white);
    letter-spacing: .3px;
  }
  .profile {
    display: flex;
    align-items: center;
    gap: 8px;
    font-size: 14px;
    color: var(--white);
    letter-spacing: .3px;
  }
  .profile-dot {
    width: 18px;
    height: 18px;
    border-radius: 50%;
    background: var(--royal-blue);
  }
</style>
</head>
<body>
  <section class="card card-back">
    <h2 class="university-name">UNIVERSITY NAME</h2>
    <p class="address">218, Campus Way, Suite 4<br>60210,Northland</p>
    <div class="divider"></div>
    <p class="contact">
      044-987 654 321<br>
      info@kmstudio.com<br>
      www.<span class="accent">kmcardsite</span>.com
    </p>
  </section>

  <section class="card card-front">
    <div class="monogram">KM</div>
    <h1 class="person-name">KAYLA MORGAN</h1>
    <p class="program">Business Marketing</p>
    <div class="divider"></div>
    <p class="profile"><span class="profile-dot"></span>network.com/kmorgan</p>
  </section>
</body>
</html>
```